Step Marmalade - a dance school theatre production

We need a visually eye catching poster design which advertises our forthcoming theatre production "Step Marmalade" Sized A2

Our dance school is professional yet funky and modern, and we wish to portray this visually.

This has to be vibrant and colourful, with the school name and production name being the initial eye catching theme.

Our dance school name is the Welloby-Crane School of Dance

Our dance school offers a variety of dance styles including ballet,tap,street, jazz,rock and roll

Requirements
Must have
• "Step Marmalade" as the production name
www.wcschoolofdance.example
Ashgrove Lantern Theatre 01632 960417
30th September 2011-1st October 2011
price; £8 adults , £7 concessions
tickets available from the theatre box office
Nice to have
• an eye catching main image incorporated into the design?
Should not have
• no flowery fonts please

```html
<!DOCTYPE html>
<html lang="en">
<head>
<meta charset="utf-8">
<title>Step Marmalade – Welloby-Crane School of Dance</title>
<link rel="stylesheet" href="https://fonts.googleapis.com/css2?family=Caprasimo&display=swap">
<style>
  :root {
    --page: #ffffff;
    --ink: #ffffff;
    --ink-soft: #fde3ea;
    --band-dark: #1e0a10;
    --band-mid: #6b1f33;
    --band-pink: #e07796;
    --candy-green: #3fa046;
    --candy-lime: #8fd35a;
    --candy-blue: #2f5fc4;
    --candy-purple: #6b3a9e;
    --candy-red: #d3122c;
    --candy-orange: #f2641b;
    --candy-yellow: #f5c81f;
  }
  * { margin: 0; padding: 0; box-sizing: border-box; }
  html, body {
    width: 1200px; height: 900px; overflow: hidden;
    background: var(--page);
  }
  .poster {
    position: absolute;
    left: 314px; top: 35px;
    width: 572px; height: 830px;
    overflow: hidden;
    font-family: "Caprasimo", Georgia, serif;
    color: var(--ink);
  }
  .poster__art { position: absolute; inset: 0; width: 100%; height: 100%; }
  .poster__text {
    position: absolute;
    white-space: nowrap;
    transform: translate(-50%, -50%) rotate(var(--tilt, -22deg));
    line-height: 1;
  }
  .school-name { left: 235px; top: 292px; font-size: 23px; }
  .title-step { left: 215px; top: 385px; font-size: 150px; }
  .title-marmalade { left: 300px; top: 485px; font-size: 92px; }
  .info { --tilt: -28deg; color: var(--ink-soft); }
  .info--web { left: 430px; top: 520px; font-size: 15px; }
  .info--tickets { left: 410px; top: 556px; font-size: 16px; }
  .info--venue { left: 395px; top: 600px; font-size: 15px; }
  .info--dates { left: 300px; top: 668px; font-size: 19px; }
  .info--price { left: 250px; top: 720px; font-size: 18px; }
  .info--price small { font-size: 13px; }
</style>
</head>
<body>
<main class="poster">
  <svg class="poster__art" viewBox="0 0 572 830" aria-hidden="false">
    <defs>
      <linearGradient id="candyCool" x1="0" y1="0" x2="1" y2="1">
        <stop offset="0" stop-color="var(--candy-lime)"/>
        <stop offset="0.35" stop-color="var(--candy-green)"/>
        <stop offset="0.65" stop-color="var(--candy-blue)"/>
        <stop offset="1" stop-color="var(--candy-purple)"/>
      </linearGradient>
      <linearGradient id="candyWarm" x1="0" y1="1" x2="1" y2="0">
        <stop offset="0" stop-color="var(--candy-red)"/>
        <stop offset="0.5" stop-color="var(--candy-orange)"/>
        <stop offset="0.8" stop-color="var(--candy-yellow)"/>
        <stop offset="1" stop-color="var(--candy-orange)"/>
      </linearGradient>
      <linearGradient id="band" x1="0" y1="1" x2="1" y2="0">
        <stop offset="0.15" stop-color="var(--band-dark)"/>
        <stop offset="0.5" stop-color="var(--band-mid)"/>
        <stop offset="0.85" stop-color="var(--band-pink)"/>
      </linearGradient>
    </defs>
    <rect class="candy candy--warm" width="572" height="830" fill="url(#candyWarm)"
          role="img" aria-label="Photograph of red, orange and yellow sweets and jelly beans"/>
    <path class="candy candy--cool" d="M0 0 H420 C330 120 160 240 0 300 Z" fill="url(#candyCool)"
          role="img" aria-label="Photograph of green, blue and purple sweets and jelly beans"/>
    <path class="swoosh-band" d="M420 0 H572 V280 C380 360 180 500 0 630 V300 C160 240 330 120 420 0 Z"
          fill="url(#band)"/>
  </svg>

  <p class="poster__text school-name">Welloby-Crane School of Dance</p>
  <h1 class="poster__text title-step">Step</h1>
  <h1 class="poster__text title-marmalade">Marmalade</h1>

  <p class="poster__text info info--web">www.wcschoolofdance.example</p>
  <p class="poster__text info info--tickets">tickets available from the theatre box office</p>
  <p class="poster__text info info--venue">Ashgrove Lantern Theatre 01632 960417</p>
  <p class="poster__text info info--dates">30th September 2011–1st October 2011</p>
  <p class="poster__text info info--price">price; £8 <small>adults , £7 concessions</small></p>
</main>
</body>
</html>
```